Container for chopstick set. Box or cylinder

The package will hold 5 pairs of black chopsticks (see uploaded file). These are the things that we liked from the attached files:
Idea 1: Kraft paper, illustration, the contrast of the green color with black illustration + text and green background
Idea 2: cylinder
Idea 3: Illustration of product, slide opening box type

Target Market(s)

The target market are women with families around between the ages of 25-50.

Font styles to use
Other font styles liked:
• Please see logo

Colors

Designer to choose colors to be used in the design.

Requirements
Must have
• Please incorporate our logo into the package (it's ok to change the colors of our logo), but our logo shouldn't cover a significant surface of the package
• Be creative with color(s).
Nice to have
• Possible designs:
• 1) Cylinder (4cm diameter, 25cm height)
• Alternative A: black matte background
• Alternative B: similar colors in Idea 1 with Kraft paper background.
• 2) Slide opening box (7cm x 25cm x 1cm)
• Alternative C: white box which incorporates our green logo (bottom right)

```html
<!DOCTYPE html>
<html lang="en">
<head>
<meta charset="utf-8">
<title>Fernlow Chopstick Tube Label</title>
<link rel="stylesheet" href="https://fonts.googleapis.com/css2?family=Montserrat:wght@500&family=Oswald:wght@400&display=swap">
<style>
  :root {
    --page-bg: #f4f5f7;
    --gold-dark: #a2602a;
    --gold-mid: #d79a3f;
    --gold-light: #f4d27a;
    --copper: #8f4a28;
    --matte-black: #2f2e30;
    --matte-edge: #1f1e20;
    --leaf-green: #9fd46b;
    --label-white: #ffffff;
    --ink: #141414;
  }
  html, body {
    margin: 0;
    width: 964px;
    height: 1200px;
    overflow: hidden;
    background: var(--page-bg);
  }
  .canvas {
    position: relative;
    width: 964px;
    height: 1200px;
  }
  .tube-label {
    position: absolute;
    left: 348px;
    top: 150px;
    width: 272px;
    height: 922px;
    overflow: hidden;
    box-shadow: 0 6px 14px rgba(0,0,0,0.12);
  }
  .brand-band {
    position: absolute;
    left: 0;
    right: 0;
    top: 0;
    height: 174px;
    background: linear-gradient(90deg, var(--gold-dark) 0%, var(--gold-mid) 30%, var(--gold-light) 52%, var(--gold-mid) 72%, var(--copper) 100%);
  }
  .brand-dot {
    position: absolute;
    left: 110px;
    top: 56px;
    width: 52px;
    height: 52px;
    border-radius: 50%;
    background: var(--leaf-green);
  }
  .brand-name {
    position: absolute;
    left: 0;
    right: 0;
    top: 132px;
    text-align: center;
    font-family: "Montserrat", sans-serif;
    font-weight: 500;
    font-size: 28px;
    letter-spacing: 0.5px;
    color: var(--label-white);
    line-height: 1;
  }
  .blossom-field {
    position: absolute;
    left: 0;
    right: 0;
    top: 174px;
    bottom: 0;
    background: linear-gradient(90deg, var(--matte-edge) 0%, var(--matte-black) 25%, #3a393b 55%, var(--matte-black) 80%, var(--matte-edge) 100%);
  }
  .product-panel {
    position: absolute;
    left: 62px;
    top: 382px;
    width: 148px;
    bottom: 0;
    border-radius: 30px 30px 0 0;
    background: linear-gradient(90deg, var(--gold-dark) 0%, var(--gold-mid) 28%, var(--gold-light) 50%, var(--gold-mid) 72%, var(--copper) 100%);
    display: flex;
    align-items: flex-end;
    justify-content: center;
    padding: 40px 0 28px;
    box-sizing: border-box;
  }
  .product-title {
    margin: 0;
    font-family: "Oswald", sans-serif;
    font-weight: 400;
    font-size: 46px;
    line-height: 1;
    letter-spacing: -1.5px;
    color: var(--ink);
    writing-mode: vertical-rl;
    transform: rotate(180deg);
    white-space: nowrap;
  }
</style>
</head>
<body>
  <main class="canvas">
    <section class="tube-label">
      <header class="brand-band">
        <div class="brand-dot"></div>
        <span class="brand-name">Fernlow</span>
      </header>
      <div class="blossom-field" role="img" aria-label="Gold cherry blossom branches scattered across a matte black background"></div>
      <div class="product-panel">
        <h1 class="product-title">5 PAIRS OF BLACK CHOPSTICKS</h1>
      </div>
    </section>
  </main>
</body>
</html>
```